Marlowe Restoration & Remodeling Group LLC

Roofing, windows, gutters services offered.
0% 6 months interest free financing
Vernon windows
Whitfield windows
KTR roofing shingles
ULP roofing shingles
Offering 30-50 year warranties.
Accepting all major credit cards, checks
Emergency services available

Target Market(s)

Roofing contractors

Industry/Entity Type

Roofing

Number of Pages Required

3 page

Font styles to use
Sans Serif

Requirements
Must have
• MUST HAVE SEO all necessary codes!!!!!!!!!!
• also I want button for "schedule appointment" so I can receive notification of an appointment, and also need live calendar integrated in that button
Nice to have
• Modern, professional site

```html
<!DOCTYPE html>
<html lang="en">
<head>
<meta charset="utf-8">
<title>Marlowe Restoration &amp; Remodeling Group LLC | Roofing, Windows &amp; Gutters</title>
<meta name="description" content="Marlowe Restoration & Remodeling Group LLC: roofing, windows and gutter services with 0% financing, 30-50 year warranties and emergency service.">
<meta name="viewport" content="width=1200">
<link href="https://fonts.googleapis.com/css2?family=Alegreya:wght@500;700&family=Alegreya+SC:wght@500&family=Lato:ital,wght@0,400;0,700;1,400&display=swap" rel="stylesheet">
<style>
:root{
  --teal:#1a9497;
  --teal-dark:#147a7d;
  --navy:#1b2d5b;
  --ink:#222831;
  --muted:#6d7178;
  --page:#f2f2f2;
  --white:#ffffff;
  --line:#d9d9d9;
}
*{box-sizing:border-box;margin:0;padding:0}
html,body{width:1200px;height:4021px;overflow:hidden}
body{background:var(--page);font-family:'Lato',sans-serif;color:var(--ink);position:relative}
.abs{position:absolute}
.serif{font-family:'Alegreya',serif}
.btn{position:absolute;background:var(--teal);color:var(--white);font-family:'Alegreya',serif;font-weight:700;display:flex;align-items:center;justify-content:center;text-decoration:none}
.btn::before,.btn::after{content:"";position:absolute;width:24px;height:24px;border:2px solid var(--teal)}
.btn::before{left:-5px;top:-5px;border-right:none;border-bottom:none}
.btn::after{right:-5px;top:-5px;border-left:none;border-bottom:none}
.eyebrow{font-size:14px;font-weight:700;letter-spacing:.2px;text-transform:uppercase;color:var(--ink)}
.section-title{font-family:'Alegreya',serif;font-weight:700;color:var(--teal);font-size:44px;line-height:1}
.lorem{font-size:12px;line-height:20px;color:var(--muted)}

/* header */
.site-header{left:0;top:0;width:1200px;height:90px;background:var(--white)}
.brand{left:162px;top:16px;display:flex;align-items:center;gap:10px}
.brand-mark{width:22px;height:22px;border-radius:50%;background:var(--teal)}
.brand-name{font-family:'Alegreya',serif;font-weight:700;font-size:13px;line-height:15px;color:var(--navy)}
.nav{right:162px;top:31px;display:flex;gap:0}
.nav a{font-family:'Alegreya',serif;font-size:13px;color:var(--teal);text-decoration:none;padding:0 14px;height:30px;line-height:30px}
.nav a.active{background:var(--teal);color:var(--white)}

/* hero */
.hero{left:0;top:90px;width:1200px;height:578px;background:linear-gradient(160deg,#3a4550 0%,#2a3540 45%,#1d2a36 100%)}
.hero-title{left:164px;top:212px;font-family:'Alegreya SC',serif;font-weight:500;font-size:60px;line-height:63px;color:var(--white)}
.hero-photo{left:723px;top:203px;width:477px;height:410px;background:linear-gradient(150deg,#4d5864 0%,#6b7580 50%,#c9c3b6 100%)}
.slide-dots{left:1143px;top:345px}
.slide-count{left:937px;top:582px;color:var(--white);font-family:'Alegreya',serif;font-weight:700;font-size:19px}
.slide-count small{font-size:11px}

/* help band */
.help-band{left:0;top:668px;width:1200px;height:120px;background:var(--navy)}
.help-title{left:164px;top:692px;font-family:'Alegreya',serif;font-weight:700;font-size:22px;color:var(--white)}
.help-text{left:164px;top:724px;width:500px;font-size:11px;line-height:20px;color:#c8cfe0}

/* services */
.services-head{left:0;top:855px;width:1200px;text-align:center}
.service-cards{left:161px;top:960px;width:877px;height:278px;background:var(--white);border:1px solid var(--line);display:flex}
.service{flex:1;text-align:center;padding:34px 14px 0}
.service.featured{background:var(--teal)}
.service h3{font-family:'Alegreya',serif;font-weight:700;font-size:19px;margin:18px 0 14px;color:var(--ink)}
.service.featured h3{color:var(--white)}
.service p{font-size:11.5px;line-height:20px;color:var(--muted)}
.service.featured p{color:#d3eeee}

/* about */
.about-photo{left:0;top:1327px;width:751px;height:412px;background:linear-gradient(135deg,#6b4a30 0%,#9c7a5a 40%,#b9c8e3 60%,#a7bde0 100%)}
.about-strip{left:0;top:1327px;width:225px;height:412px;background:var(--teal);opacity:.92}
.slider-arrows{left:187px;top:1702px;width:75px;height:37px;background:var(--white);display:flex;align-items:center;justify-content:space-around}
.about-card{left:663px;top:1394px;width:377px;height:345px;background:var(--white);padding:36px 36px 0}
.tick-list{list-style:none}
.tick-list li{font-family:'Alegreya',serif;font-weight:700;font-size:12.5px;color:var(--navy);display:flex;align-items:center;gap:14px}
.tick-list li::before{content:"";width:9px;height:9px;border-radius:50%;background:var(--navy);box-shadow:0 0 0 3px #c9d0e0}

/* more services */
.more-photo{left:439px;top:1817px;width:601px;height:375px;background:linear-gradient(120deg,#a9b4c2 0%,#7f8a99 50%,#4e5866 100%)}
.more-card{left:161px;top:1895px;width:376px;height:300px;background:var(--white);padding:28px 22px 0}
.more-card .tick-list li{margin-bottom:23px}

/* testimonials */
.testi-photo{left:0;top:2263px;width:1200px;height:375px;background:linear-gradient(90deg,#8a7f6e 0%,#b8a78a 30%,#c2807a 60%,#5b6486 100%)}
.testi-card{left:514px;top:2337px;width:526px;height:301px;background:var(--white);padding:28px 28px 0}
.client-photo{left:536px;top:2453px;width:98px;height:112px;background:linear-gradient(160deg,#9fb3c7,#3e4b5e);border:3px solid #c9d6e4}
.client-name{left:652px;top:2482px;font-family:'Alegreya',serif;font-weight:700;font-size:12px;color:var(--navy)}
.client-quote{left:647px;top:2505px;width:330px;font-style:italic;font-size:11px;line-height:20px;color:var(--muted)}

/* warranty */
.warranty{left:225px;top:2686px;width:751px;height:186px;background:var(--white)}
.warranty-num{left:36px;top:10px;font-family:'Alegreya',serif;font-weight:700;font-size:158px;line-height:1;color:#dcdcdc}
.warranty-title{left:210px;top:42px;font-family:'Alegreya',serif;font-weight:700;font-size:45px;color:var(--teal)}
.warranty-text{left:216px;top:108px;width:500px;font-size:11px;line-height:20px;color:var(--muted)}

/* contact */
.contact-head{left:0;top:2932px;width:1200px;text-align:center}
.field{position:absolute;background:var(--white);border:1px solid var(--line);font-size:11.5px;color:var(--muted);padding:14px 12px}

/* newsletter */
.newsletter{left:0;top:3425px;width:1200px;height:112px;background:var(--navy)}
.newsletter-title{left:164px;top:3463px;font-family:'Alegreya',serif;font-weight:700;font-size:31px;color:var(--white)}
.news-input{left:612px;top:3459px;width:301px;height:42px;background:var(--white);font-size:11px;color:var(--muted);padding:14px 12px}
.news-btn{left:913px;top:3459px;width:126px;height:42px;background:var(--teal);color:var(--white);font-family:'Alegreya',serif;font-weight:700;font-size:13px;display:flex;align-items:center;justify-content:center}

/* footer */
.footer-brand{left:0;top:3625px;width:1200px;display:flex;justify-content:center;align-items:center;gap:10px}
.footer-nav{left:0;top:3726px;width:1200px;display:flex;justify-content:center;gap:24px;font-size:12px;color:var(--muted)}
.footer-col h4{font-family:'Alegreya',serif;font-weight:700;font-size:15px;color:var(--navy)}
.footer-col h4.teal{color:var(--teal)}
.contact-row{display:flex;gap:14px;align-items:flex-start;font-size:11.5px;line-height:16px;color:var(--muted);margin-bottom:20px}
.social-row{display:flex;gap:14px;align-items:center;font-size:12px;color:var(--teal);margin-bottom:12px}
.social-dot{width:26px;height:26px;border-radius:50%;border:1.5px solid var(--teal)}
.social-dot.filled{background:var(--teal)}
.card-badges{display:flex;gap:7px;margin-top:18px}
.card-badges span{width:34px;height:22px;background:var(--teal);border-radius:2px}
.copyright{left:0;top:3976px;width:1200px;height:45px;background:var(--teal);color:var(--white);font-size:11.5px;display:flex;align-items:center;justify-content:center}
</style>
</head>
<body>

<header class="abs site-header">
  <div class="abs brand">
    <span class="brand-mark"></span>
    <span class="brand-name">Marlowe<br>Restoration &amp; Remodeling<br>Group LLC</span>
  </div>
  <nav class="abs nav" aria-label="Main">
    <a class="active" href="#">Home</a><a href="#">About Us</a><a href="#">Services</a><a href="#">Testimonials</a><a href="#">Contact Us</a>
  </nav>
</header>

<section class="abs hero" role="img" aria-label="Dusk photo of a large white house behind trees"></section>
<h1 class="abs hero-title">Marlowe<br>Restoration<br>Remodeling<br>Group LLC</h1>
<a class="btn" href="#contact" style="left:164px;top:506px;width:129px;height:53px;font-size:17px">Contact Us</a>
<div class="abs hero-photo" role="img" aria-label="Photo of a cream house gable against a dark sky"></div>
<svg class="abs slide-dots" width="57" height="130" viewBox="0 0 57 130" aria-hidden="true">
  <g fill="none" stroke="#fff" stroke-width="1.3">
    <path d="M9 2l6 6-6 6-6-6z"/><path d="M9 40l6 6-6 6-6-6z"/><path d="M9 116l6 6-6 6-6-6z"/>
    <line x1="24" y1="8" x2="57" y2="8"/><line x1="24" y1="46" x2="57" y2="46"/><line x1="24" y1="84" x2="57" y2="84"/><line x1="24" y1="122" x2="57" y2="122"/>
  </g>
  <path d="M-20 71l7 7-7 7-7-7z" fill="#fff" transform="translate(0,0)"/>
</svg>
<div class="abs slide-count">02<small> / 04</small></div>

<section class="abs help-band"></section>
<h2 class="abs help-title">We Help to Improve Your Roofing, Windows etc..</h2>
<p class="abs help-text">Lorem Ipsum is simply dummy text of the printing and typesetting industry. Lorem Ipsum has been the industry's standard dummy text ever since the 1500s</p>
<a class="btn" href="#" style="left:845px;top:710px;width:190px;height:39px;font-size:13.5px">Schedule An Appointment</a>

<section class="abs services-head">
  <p class="eyebrow">Our Services</p>
  <h2 class="section-title" style="margin-top:8px">What We Provide</h2>
</section>
<div class="abs service-cards">
  <article class="service">
    <svg width="66" height="56" viewBox="0 0 66 56" aria-hidden="true" fill="none" stroke="var(--teal)" stroke-width="2.5"><path d="M4 54h58M8 54L24 6h20l18 48M24 6l14 48M30 6l16 48"/><path d="M14 54V40a5 5 0 0 1 10 0v14"/></svg>
    <h3>Roofing</h3>
    <p>Lorem Ipsum is simply dummy text of the printing and typesetting industry. Lorem Ipsum has been the industry's standard dummy text ever since the 1500s.</p>
  </article>
  <article class="service featured">
    <svg width="60" height="56" viewBox="0 0 60 56" aria-hidden="true" fill="none" stroke="#fff" stroke-width="2.5"><rect x="4" y="4" width="52" height="48"/><rect x="10" y="10" width="22" height="36"/><path d="M38 4v48M46 14v30"/></svg>
    <h3>Windows</h3>
    <p>Lorem Ipsum is simply dummy text of the printing and typesetting industry. Lorem Ipsum has been the industry's standard dummy text ever since the 1500s.</p>
  </article>
  <article class="service">
    <svg width="50" height="56" viewBox="0 0 50 56" aria-hidden="true" fill="none" stroke="var(--teal)" stroke-width="2.5"><path d="M4 4h16v12H4zM14 16v10h14v-6h10v16H28v-4H14M28 36v8h14v10H28z"/></svg>
    <h3>Gutter</h3>
    <p>Lorem Ipsum is simply dummy text of the printing and typesetting industry. Lorem Ipsum has been the industry's standard dummy text ever since the 1500s.</p>
  </article>
</div>

<div class="abs about-photo" role="img" aria-label="Photo looking up at a roof corner against a blue sky"></div>
<div class="abs about-strip"></div>
<div class="abs slider-arrows">
  <svg width="12" height="14" viewBox="0 0 12 14" aria-hidden="true"><path d="M9 1L3 7l6 6" fill="none" stroke="var(--navy)" stroke-width="1.8"/></svg>
  <svg width="12" height="14" viewBox="0 0 12 14" aria-hidden="true"><path d="M3 1l6 6-6 6" fill="none" stroke="var(--navy)" stroke-width="1.8"/></svg>
</div>
<section class="abs about-card">
  <p class="eyebrow">Know More</p>
  <h2 class="section-title" style="font-size:46px;margin:10px 0 18px">About Us</h2>
  <p class="lorem" style="font-size:11.5px">Lorem Ipsum is simply dummy text of the printing and typesetting industry. Lorem Ipsum has been the industry's standard dummy text ever since the 1500s, when an unknown printer took a galley of type and scrambled it to make a type specimen book.</p>
  <ul class="tick-list" style="margin-top:12px"><li>Emergency services available</li></ul>
</section>
<a class="btn" href="#" style="left:694px;top:1675px;width:105px;height:37px;font-size:13.5px">Learn More</a>

<div class="abs more-photo" role="img" aria-label="Photo of a roofer in a hard hat and safety vest laying roof shingles"></div>
<section class="abs more-card">
  <p class="eyebrow" style="font-size:13.5px">0% 6 Months Interest Free Financing</p>
  <h2 class="section-title" style="margin:12px 0 24px">More Services</h2>
  <ul class="tick-list">
    <li>Vernon windows</li><li>Whitfield windows</li><li>KTR roofing shingles</li><li>ULP roofing shingles</li>
  </ul>
</section>

<div class="abs testi-photo" role="img" aria-label="Photo of a suburban house with a garage under a pink sunset sky"></div>
<section class="abs testi-card">
  <p class="eyebrow">Testimonials</p>
  <h2 class="section-title" style="margin-top:12px">What Our Clients Say</h2>
</section>
<div class="abs client-photo" role="img" aria-label="Client portrait"></div>
<p class="abs client-name">-CLIENT NAME</p>
<p class="abs client-quote">Lorem Ipsum is simply dummy text of the printing and typesetting industry. Lorem Ipsum has been the industry's standard dummy text ever since the 1500s, when an unknown printer took a galley of type and scrambled it to make a type specimen book.</p>
<svg class="abs" style="left:557px;top:2585px" width="60" height="12" viewBox="0 0 60 12" aria-hidden="true">
  <g stroke="var(--teal)" stroke-width="1.3"><path d="M6 1l5 5-5 5-5-5z" fill="none"/><path d="M30 1l5 5-5 5-5-5z" fill="var(--navy)" stroke="var(--navy)"/><path d="M54 1l5 5-5 5-5-5z" fill="none"/></g>
</svg>

<section class="abs warranty">
  <div class="abs warranty-num">30</div>
  <h2 class="abs warranty-title">Year Warranties We Offer</h2>
  <p class="abs warranty-text">Lorem Ipsum is simply dummy text of the printing and typesetting industry. Lorem Ipsum has been the industry's standard dummy text ever since the 1500s</p>
</section>

<section class="abs contact-head" id="contact">
  <p class="eyebrow">Contact Us</p>
  <h2 class="section-title" style="margin-top:10px">Get In Touch</h2>
</section>
<div class="field" style="left:326px;top:3061px;width:262px;height:44px">Name:</div>
<div class="field" style="left:604px;top:3061px;width:262px;height:44px">Email:</div>
<div class="field" style="left:326px;top:3122px;width:262px;height:42px">Phone No:</div>
<div class="field" style="left:604px;top:3122px;width:262px;height:42px">Subject:</div>
<div class="field" style="left:326px;top:3181px;width:540px;height:88px">Message:</div>
<a class="btn" href="#" style="left:539px;top:3317px;width:123px;height:39px;font-size:13.5px">Send Message</a>

<section class="abs newsletter"></section>
<h2 class="abs newsletter-title">Subscribe To Our Newsletter</h2>
<div class="abs news-input">Email:</div>
<div class="abs news-btn">Subscribe Now!</div>

<footer>
  <div class="abs footer-brand">
    <span class="brand-mark"></span>
    <span class="brand-name">Marlowe<br>Restoration &amp; Remodeling<br>Group LLC</span>
  </div>
  <nav class="abs footer-nav" aria-label="Footer"><span>Home</span><span>About Us</span><span>Services</span><span>Testimonials</span><span>Contact Us</span></nav>

  <div class="abs footer-col" style="left:162px;top:3770px;width:200px">
    <h4>About Us</h4>
    <p class="lorem" style="font-size:11.5px;margin-top:28px">Lorem Ipsum is simply dummy text of the printing and typesetting industry. Lorem Ipsum has been the.</p>
    <div class="card-badges" aria-label="Accepted payment cards"><span></span><span></span><span></span><span></span><span></span></div>
  </div>

  <div class="abs footer-col" style="left:387px;top:3770px;width:200px">
    <h4 class="teal" style="font-size:14px">Contact Info</h4>
    <div style="margin-top:24px">
      <div class="contact-row"><svg width="20" height="18" viewBox="0 0 20 18" aria-hidden="true"><path d="M4 1l4 4-2 2c1 3 3 5 6 6l2-2 4 4-2 2C8 17 2 11 2 3z" fill="var(--navy)"/></svg>+1-555-014-2290</div>
      <div class="contact-row"><svg width="20" height="14" viewBox="0 0 20 14" aria-hidden="true"><rect x="1" y="1" width="18" height="12" fill="var(--navy)"/><path d="M1 1l9 7 9-7" fill="none" stroke="#fff" stroke-width="1.3"/></svg>support@marloweremodeling.com</div>
      <div class="contact-row"><svg width="20" height="24" viewBox="0 0 20 24" aria-hidden="true"><path d="M10 1a7 7 0 0 1 7 7c0 6-7 14-7 14S3 14 3 8a7 7 0 0 1 7-7z" fill="var(--navy)"/><circle cx="10" cy="8" r="2.5" fill="#fff"/></svg><span>100-Lorem ipsum is simply<br>dummy text.</span></div>
    </div>
  </div>

  <div class="abs footer-col" style="left:612px;top:3770px;width:200px">
    <h4>Follow Us on</h4>
    <div style="margin-top:22px">
      <div class="social-row"><span class="social-dot filled"></span>Friendbook</div>
      <div class="social-row"><span class="social-dot"></span>LinkUp</div>
      <div class="social-row"><span class="social-dot"></span>Searchly</div>
      <div class="social-row"><span class="social-dot"></span>Chirper</div>
    </div>
  </div>

  <div class="abs footer-col" style="left:838px;top:3812px;width:200px">
    <h4 style="font-size:14px;line-height:18px">Emergency Services<br>Available</h4>
  </div>
  <a class="btn" href="#" style="left:841px;top:3880px;width:120px;height:34px;font-size:12.5px">+1-555-014-2290</a>

  <div class="abs copyright">Copyright©2019 Marlowe. All Right Reserved. Terms &amp; Conditions.</div>
</footer>

</body>
</html>
```